Property risk and finance brokerage company needs a business card design

Tarn Financial requires a business card design. Please integrate existing logo (refer uploaded file).
hex codes used on logo #002649 #008ED6 #444F51 #ADAFAA
font used - Cinzel
Contact information
Roslyn Venterelli
Director
Mobile: 0471 385 902
email: r.venterelli@tarnfinancial.com.au
website: www.tarnfinancial.com.au
CRN : 815390
PO Box 547
Kelmscott, Victoria, 3188
Horizontal orientation please

```html
<!DOCTYPE html>
<html lang="en">
<head>
<meta charset="utf-8">
<title>Tarn Financial – Business Card</title>
<link rel="stylesheet" href="https://fonts.googleapis.com/css2?family=Cinzel:wght@400;700&family=Lato:wght@300;400&display=swap">
<style>
  :root {
    --navy: #002649;
    --band: #0b2340;
    --blue: #008ed6;
    --name-blue: #0b5c9a;
    --link-blue: #0b6fb0;
    --slate: #444f51;
    --grey: #adafaa;
    --paper: #ffffff;
    --edge: #555555;
  }
  * { margin: 0; padding: 0; box-sizing: border-box; }
  html, body {
    width: 1000px; height: 1200px; overflow: hidden;
    background: var(--paper);
  }
  .sheet { position: relative; width: 1000px; height: 1200px; }

  .card {
    position: absolute; left: 150px; width: 700px; height: 400px;
    border: 1px solid var(--edge); background: var(--paper); overflow: hidden;
  }
  .card--front { top: 154px; }
  .card--back { top: 646px; }

  /* Front: wordmark */
  .wordmark {
    position: absolute; inset: 0;
    display: flex; align-items: center; justify-content: center; gap: 22px;
  }
  .wordmark__dot {
    width: 62px; height: 62px; border-radius: 50%;
    background: var(--blue);
  }
  .wordmark__name {
    font-family: "Cinzel", serif; font-weight: 400;
    font-size: 50px; color: var(--navy); letter-spacing: 1px;
  }

  /* Back */
  .emblem {
    position: absolute; left: 420px; top: 40px; width: 260px; height: 260px;
    border-radius: 50%;
    background: radial-gradient(circle at 45% 40%, rgba(0,142,214,0.16), rgba(0,38,73,0.08));
    z-index: 0;
  }
  .contact { position: absolute; left: 51px; top: 132px; color: var(--slate); z-index: 1; }
  .contact__name {
    font-family: "Cinzel", serif; font-size: 30px; line-height: 34px;
    color: var(--navy); font-weight: 400;
  }
  .contact__first { font-weight: 700; color: var(--name-blue); }
  .contact__role {
    font-family: "Lato", sans-serif; font-weight: 400;
    font-size: 22px; color: var(--slate); margin-top: 0;
  }
  .contact__list { list-style: none; margin-top: 40px; }
  .contact__item { line-height: 30.5px; white-space: nowrap; }
  .contact__label { font-family: "Cinzel", serif; font-size: 23px; color: var(--slate); }
  .contact__value { font-family: "Lato", sans-serif; font-weight: 300; font-size: 23px; color: var(--slate); }
  .contact__value--accent { font-weight: 400; color: var(--link-blue); }

  .address-band {
    position: absolute; left: 0; right: 0; bottom: 0; height: 60px;
    background: var(--band); color: var(--paper);
    display: flex; align-items: center; padding-left: 51px;
    font-size: 24px; white-space: nowrap; z-index: 1;
  }
  .address-band__box { font-family: "Lato", sans-serif; font-weight: 300; }
  .address-band__sep { font-family: "Lato", sans-serif; font-weight: 300; margin: 0 24px; }
  .address-band__place { font-family: "Cinzel", serif; }
</style>
</head>
<body>
<main class="sheet">
  <section class="card card--front" aria-label="Card front">
    <div class="wordmark">
      <span class="wordmark__dot" aria-hidden="true"></span>
      <span class="wordmark__name">Tarn Financial</span>
    </div>
  </section>

  <section class="card card--back" aria-label="Card back">
    <div class="emblem" role="img" aria-label="Brand emblem area"></div>
    <div class="contact">
      <h1 class="contact__name"><span class="contact__first">Roslyn</span> Venterelli</h1>
      <p class="contact__role">Managing Director</p>
      <ul class="contact__list">
        <li class="contact__item"><span class="contact__label">Mobile: </span><span class="contact__value contact__value--accent">0471.385.902</span></li>
        <li class="contact__item"><span class="contact__label">Email: </span><span class="contact__value">r.venterelli@tarnfinancial.com.au</span></li>
        <li class="contact__item"><span class="contact__label">Credit Rep No. : </span><span class="contact__value">000.000.000</span></li>
      </ul>
    </div>
    <div class="address-band">
      <span class="address-band__box">PO Box 547</span>
      <span class="address-band__sep">|</span>
      <span class="address-band__place">Kelmscott, Victoria, 3188</span>
    </div>
  </section>
</main>
</body>
</html>
```